Design a Professional Business Card for Velmora Arcs

Design a business card for Velmora Arcs, we are a National Sport Court Company.

West Region Address: 4175 Quill Harbor Ln, Suite #215 Englewood, Colorado 80467
East Region Address: 3817 Tamsin Rd E, Bradenton, Florida 34583

Target Market(s)

High End Residential & Institutional Clients

Industry/Entity Type

Design & Construction

Contact Information for Business Card

Logo/Brand/Colors/ name, number (provided in comments)

Requirements
Must have
• Colors only provided in logo
Should not have
• Any other colors not in existing logo (attached)

```html
<!DOCTYPE html>
<html lang="en">
<head>
<meta charset="utf-8">
<title>Velmora Arcs – Business Card</title>
<link href="https://fonts.googleapis.com/css2?family=Poppins:wght@400;600;700&display=swap" rel="stylesheet">
<style>
  :root {
    --navy: #1c3566;
    --green: #176b3a;
    --white: #ffffff;
    --stage: #e9ebee;
    --shadow: rgba(20, 30, 50, 0.18);
  }
  * { margin: 0; padding: 0; box-sizing: border-box; }
  html, body { width: 1200px; height: 1200px; overflow: hidden; }
  body {
    background: var(--stage);
    font-family: "Poppins", sans-serif;
    position: relative;
  }
  .card {
    position: absolute;
    left: 160px;
    width: 880px;
    height: 503px;
    overflow: hidden;
    box-shadow: 0 10px 30px var(--shadow);
  }
  .card-front {
    top: 67px;
    background: linear-gradient(180deg, var(--navy) 0%, #1a5654 55%, var(--green) 100%);
    display: flex;
    align-items: center;
    justify-content: center;
  }
  .card-back { top: 630px; background: var(--white); }

  .brand { display: flex; align-items: center; gap: 22px; }
  .brand-mark { border-radius: 50%; flex: none; }
  .brand-name {
    font-weight: 700;
    text-transform: uppercase;
    line-height: 1;
    letter-spacing: 3px;
  }
  .card-front .brand-mark { width: 110px; height: 110px; background: var(--white); }
  .card-front .brand-name { color: var(--white); font-size: 56px; }

  .back-swoosh { position: absolute; inset: 0; width: 880px; height: 503px; }

  .card-back .brand { position: absolute; left: 60px; top: 44px; }
  .card-back .brand-mark { width: 104px; height: 104px; background: var(--navy); }
  .card-back .brand-name { color: var(--navy); font-size: 50px; }

  .person { position: absolute; left: 60px; top: 186px; }
  .person-name { color: var(--navy); font-weight: 700; font-size: 27px; letter-spacing: 1px; text-transform: uppercase; line-height: 1.1; }
  .person-title { color: var(--green); font-size: 19px; line-height: 1.3; }

  .contact-list { position: absolute; left: 60px; top: 268px; list-style: none; }
  .contact-item { display: flex; align-items: center; gap: 12px; color: var(--navy); font-size: 19px; line-height: 1.6; }
  .contact-icon { width: 22px; height: 22px; flex: none; }

  .address { position: absolute; top: 360px; }
  .address-east { left: 60px; }
  .address-west { left: 420px; }
  .address-label { color: var(--green); font-weight: 700; font-size: 17px; text-transform: uppercase; letter-spacing: 0.5px; margin-bottom: 4px; }
  .address-lines { color: var(--navy); font-size: 18px; line-height: 1.35; font-style: normal; }
  .address-divider { position: absolute; left: 396px; top: 362px; width: 2px; height: 108px; background: var(--navy); }
</style>
</head>
<body>

<section class="card card-front" aria-label="Card front">
  <div class="brand">
    <span class="brand-mark"></span>
    <span class="brand-name">Velmora Arcs</span>
  </div>
</section>

<section class="card card-back" aria-label="Card back">
  <svg class="back-swoosh" viewBox="0 0 880 503" aria-hidden="true">
    <path fill="var(--green)" d="M470 0 L640 0 C760 70 810 190 800 330 C780 200 700 70 470 0 Z"/>
    <path fill="var(--navy)" d="M650 0 L880 0 L880 503 L640 503 C760 430 820 330 812 230 C805 130 750 55 650 0 Z"/>
    <path fill="none" stroke="var(--white)" stroke-width="7" d="M650 0 C750 55 805 130 812 230 C820 330 760 430 640 503"/>
  </svg>

  <div class="brand">
    <span class="brand-mark"></span>
    <span class="brand-name">Velmora Arcs</span>
  </div>

  <div class="person">
    <p class="person-name">Dorian Pellham</p>
    <p class="person-title">Manager</p>
  </div>

  <ul class="contact-list">
    <li class="contact-item">
      <svg class="contact-icon" viewBox="0 0 22 22" aria-hidden="true">
        <circle cx="11" cy="11" r="11" fill="var(--green)"/>
        <rect x="7.5" y="5" width="7" height="12" rx="1.5" fill="none" stroke="var(--white)" stroke-width="1.6"/>
      </svg>
      <span>555-214-7083</span>
    </li>
    <li class="contact-item">
      <svg class="contact-icon" viewBox="0 0 22 22" aria-hidden="true">
        <circle cx="11" cy="11" r="11" fill="var(--green)"/>
        <rect x="5.5" y="7" width="11" height="8" fill="none" stroke="var(--white)" stroke-width="1.5"/>
        <path d="M5.5 7 L11 11.5 L16.5 7" fill="none" stroke="var(--white)" stroke-width="1.5"/>
      </svg>
      <span>hello@velmoraarcs.com</span>
    </li>
  </ul>

  <div class="address address-east">
    <p class="address-label">East Region Address</p>
    <address class="address-lines">3817 Tamsin Rd E, Bradenton,<br>Florida 34583</address>
  </div>

  <span class="address-divider"></span>

  <div class="address address-west">
    <p class="address-label">West Region Address</p>
    <address class="address-lines">4175 Quill Harbor Ln,<br>Suite #215 Englewood,<br>Colorado 80467</address>
  </div>
</section>

</body>
</html>
```